Business Cards for a start up company

We are looking for a business card design for a start up company based in Ohio. The logo is attached. We are a healthcare company. We are open to all designs but want something professional but fun; creative, not boring

Industry/Entity Type

Healthcare

```html
<!DOCTYPE html>
<html lang="en">
<head>
<meta charset="utf-8">
<title>Unity Bridge Health – Business Cards</title>
<link rel="stylesheet" href="https://fonts.googleapis.com/css2?family=Open+Sans:wght@400;600;700&display=swap">
<style>
  :root {
    --navy: #23266b;
    --navy-deep: #1b1d57;
    --glow: #1f74c4;
    --cyan: #2bb7e3;
    --green: #7cc242;
    --white: #ffffff;
    --grey: #6b6b72;
    --backdrop: #e9e7e3;
  }
  html, body {
    margin: 0;
    width: 1200px;
    height: 900px;
    overflow: hidden;
    background: var(--backdrop);
    font-family: "Open Sans", Arial, sans-serif;
  }
  .canvas {
    position: relative;
    width: 1200px;
    height: 900px;
  }
  .card {
    position: absolute;
    width: 640px;
    height: 366px;
    border-radius: 4px;
    overflow: hidden;
    box-shadow: 0 10px 28px rgba(0,0,0,0.22);
  }
  /* Back side */
  .card-back {
    left: 280px;
    top: 40px;
    background: radial-gradient(ellipse 300px 200px at 58% 38%, var(--glow) 0%, #1d4a9c 40%, var(--navy) 80%, var(--navy-deep) 100%);
  }
  .back-brand {
    position: absolute;
    left: 0; right: 0; top: 150px;
    display: flex;
    justify-content: center;
    align-items: center;
    gap: 18px;
    color: var(--white);
  }
  .brand-dot {
    width: 62px; height: 62px;
    border-radius: 50%;
    background: var(--white);
  }
  .back-brand .brand-name {
    font-size: 40px;
    font-weight: 600;
  }
  /* Front side */
  .card-front {
    left: 280px;
    top: 460px;
    background: var(--white);
  }
  .front-waves {
    position: absolute;
    inset: 0;
  }
  .front-brand {
    position: absolute;
    left: 30px; top: 26px;
    display: flex;
    align-items: center;
    gap: 10px;
    color: var(--navy);
  }
  .front-brand .brand-dot {
    width: 38px; height: 38px;
    background: var(--cyan);
  }
  .front-brand .brand-name {
    font-size: 22px;
    font-weight: 600;
  }
  .person {
    position: absolute;
    left: 40px; top: 118px;
  }
  .person-name {
    margin: 0;
    font-size: 27px;
    font-weight: 700;
    color: var(--navy);
    line-height: 1.1;
  }
  .person-role {
    margin: 0;
    font-size: 15px;
    color: var(--grey);
  }
  .contact {
    position: absolute;
    right: 24px; top: 182px;
    color: var(--white);
    text-align: right;
    font-size: 14px;
    line-height: 1.25;
  }
  .contact-address { margin: 0 22px 10px 0; }
  .contact-list {
    list-style: none;
    margin: 0; padding: 0;
  }
  .contact-list li {
    display: flex;
    justify-content: flex-end;
    align-items: center;
    gap: 8px;
    font-size: 15px;
    height: 24px;
  }
  .contact-list svg { width: 14px; height: 14px; fill: var(--white); }
</style>
</head>
<body>
<main class="canvas">

  <section class="card card-back" aria-label="Card back">
    <div class="back-brand">
      <span class="brand-dot"></span>
      <span class="brand-name">Unity Bridge Health</span>
    </div>
  </section>

  <section class="card card-front" aria-label="Card front">
    <svg class="front-waves" viewBox="0 0 640 366" preserveAspectRatio="none" aria-hidden="true">
      <path d="M0 238 C120 292 250 300 350 240 C450 178 540 140 640 140 L640 366 L0 366 Z" fill="var(--navy)"/>
      <path d="M0 190 C90 250 200 282 310 262 C220 272 110 250 0 206 Z" fill="var(--cyan)"/>
      <path d="M400 172 C480 120 570 108 640 116 L640 130 C560 124 480 138 400 172 Z" fill="var(--green)"/>
    </svg>

    <div class="front-brand">
      <span class="brand-dot"></span>
      <span class="brand-name">Unity Bridge Health</span>
    </div>

    <div class="person">
      <h1 class="person-name">Daniel R. Whitford</h1>
      <p class="person-role">Managing Member</p>
    </div>

    <div class="contact">
      <p class="contact-address">2280 Meridian Park Dr,<br>Columbus, OH 43215</p>
      <ul class="contact-list">
        <li>(555) 214-3870
          <svg viewBox="0 0 16 16"><path d="M3 1l3 3-1.5 2a9 9 0 0 0 5.5 5.5L12 10l3 3-2 2C7 15 1 9 1 3z"/></svg></li>
        <li>(555) 214-3871
          <svg viewBox="0 0 16 16"><rect x="4" y="1" width="8" height="5"/><rect x="1" y="6" width="14" height="7" rx="1"/><rect x="4" y="13" width="8" height="2"/></svg></li>
        <li>(555) 608-1942
          <svg viewBox="0 0 16 16"><path d="M4 1h8v14H4zM5.5 2.5v9h5v-9z" fill-rule="evenodd"/></svg></li>
        <li>daniel@unitybridgehealth.com
          <svg viewBox="0 0 16 16"><path d="M1 3h14v10H1zM2 4l6 5 6-5z" fill-rule="evenodd"/></svg></li>
        <li>www.unitybridgehealth.com
          <svg viewBox="0 0 16 16"><circle cx="8" cy="8" r="7"/><path d="M1 8h14M8 1v14M3 4h10M3 12h10" stroke="var(--navy)" stroke-width="1" fill="none"/></svg></li>
      </ul>
    </div>
  </section>

</main>
</body>
</html>
```